2021 Personalized Vision Poster

A beautiful, pleasing design for my 2021 vision poster. Looking probably for an infographic. Open to shortening the wording used if able. As you will notice, each color represents a different category. Let me know if you need more details. The title of each section are mostly listed, but starting with the upper left with “my primary question” going counter-clockwise: my primary question, away values and rules, life purpose, power values (red), toward values and rules, top 4 goals for 2021 (middle), and relationship vision (middle). Basically, I’m just looking for a nice font and different formatting for my words.

Requirements
Must have
• All of the sections with a majority of the words used.
Nice to have
• Infographic would be nice, if possible. More concerned with a beautiful layout of words already expressed.
Should not have
• A complete reworking of the words used.

```html
<!DOCTYPE html>
<html lang="en">
<head>
<meta charset="utf-8">
<title>2021 Live Courageously – Vision Poster</title>
<link rel="stylesheet" href="https://fonts.googleapis.com/css2?family=Bebas+Neue&display=swap">
<style>
  :root {
    --orange: #f4994f;
    --white: #ffffff;
    --display: "Bebas Neue", "Oswald", sans-serif;
  }
  * { margin: 0; padding: 0; box-sizing: border-box; }
  html, body {
    width: 848px; height: 1200px; overflow: hidden;
    background: var(--white);
  }
  .poster {
    position: relative; width: 848px; height: 1200px; overflow: hidden;
    background: var(--white);
    font-family: var(--display);
    text-transform: uppercase;
  }
  .stage {
    position: absolute; left: 0; top: 0;
    width: 848px; height: 1320px;
    transform-origin: 0 0;
    transform: skewY(-7deg);
  }
  .block, .txt, .rule { position: absolute; }
  .block { background: var(--orange); }
  .block--white { background: var(--white); }
  .rule { background: var(--white); }
  .txt { line-height: 0.86; white-space: nowrap; letter-spacing: -0.01em; }
  .txt--orange { color: var(--orange); }
  .txt--white { color: var(--white); }
  .list { list-style: none; position: absolute; color: var(--white); font-size: 20px; line-height: 29px; letter-spacing: -0.02em; white-space: nowrap; }
  .list li::before { content: "- "; }
  .label { font-size: 19px; }
</style>
</head>
<body>
<main class="poster">
  <div class="stage">

    <!-- headline -->
    <h1 class="txt txt--orange" style="left:34px; top:24px; font-size:100px;">2021</h1>
    <div class="block" style="left:0; top:118px; width:848px; height:195px;"></div>
    <div class="block" style="left:348px; top:118px; width:500px; height:224px;"></div>
    <p class="txt txt--white" style="left:6px; top:126px; font-size:124px;">Live Courageosly!</p>

    <!-- goals -->
    <div class="rule" style="left:344px; top:205px; width:4px; height:137px;"></div>
    <p class="txt txt--white" style="left:18px; top:246px; font-size:62px;">1-Rental&nbsp; 2-175lbs&nbsp; 3-Team&nbsp; 4-$250K</p>
    <p class="txt txt--white" style="right:22px; top:294px; font-size:44px;">Goals</p>
    <div class="rule" style="left:348px; top:342px; width:500px; height:4px;"></div>

    <!-- toward values & rules -->
    <div class="block" style="left:0; top:313px; width:344px; height:250px;"></div>
    <p class="txt txt--white" style="left:28px; top:322px; font-size:54px;">Values &amp;</p>
    <div class="block block--white" style="left:210px; top:372px; width:150px; height:58px;"></div>
    <p class="txt txt--orange" style="left:226px; top:376px; font-size:58px;">Rules</p>
    <ul class="list" style="left:26px; top:440px; font-size:19px; line-height:28px;">
      <li>Giving of miself and serve others,</li>
      <li>Accepting love from God or others,</li>
      <li>Doing something even when seary,</li>
      <li>Choosing to put myself first,</li>
    </ul>

    <div class="block" style="left:370px; top:346px; width:478px; height:215px;"></div>
    <ul class="list" style="left:386px; top:384px;">
      <li>Practicing vulnerability,</li>
      <li>Taking actions consistent with my identity,</li>
      <li>Getting outdoors,</li>
      <li>Going on a little or big adventure,</li>
      <li>Moving my body!</li>
    </ul>

    <!-- away values -->
    <p class="txt txt--orange label" style="left:428px; top:564px;">Avoid</p>
    <div class="block" style="left:416px; top:584px; width:432px; height:88px;"></div>
    <ul class="list" style="left:430px; top:590px; line-height:27px;">
      <li>Unrighteous anger</li>
      <li>Debilitating illusion of failure</li>
      <li>Consisten debilitating anxiety</li>
    </ul>

    <p class="txt txt--orange label" style="left:18px; top:574px;">Remember</p>
    <div class="block" style="left:0; top:594px; width:412px; height:110px;"></div>
    <ul class="list" style="left:18px; top:604px; font-size:19px; line-height:29px;">
      <li>I alone have the power to choose to be angry</li>
      <li>God has made me a conqueror – I will not fail</li>
      <li>God has given me all the inner peace I need</li>
    </ul>

    <!-- power values -->
    <div class="block" style="left:0; top:704px; width:440px; height:96px;"></div>
    <div class="block" style="left:0; top:704px; width:222px; height:190px;"></div>
    <p class="txt txt--white" style="left:-6px; top:716px; font-size:200px;">Joy</p>
    <p class="txt txt--white" style="left:226px; top:706px; font-size:108px;">Love</p>
    <p class="txt txt--orange" style="left:230px; top:806px; font-size:74px;">Respect</p>

    <!-- relationship vision -->
    <p class="txt txt--orange" style="left:454px; top:690px; font-size:62px;">Relationship<br>Vision</p>
    <div class="block" style="left:470px; top:806px; width:378px; height:214px;"></div>
    <p class="txt txt--white" style="left:486px; top:814px; font-size:116px;">Power</p>
    <p class="txt txt--white" style="left:486px; top:908px; font-size:120px;">Courage</p>
    <p class="txt txt--orange" style="left:508px; top:1024px; font-size:60px;">Romantic</p>
    <div class="block" style="left:650px; top:1080px; width:198px; height:50px;"></div>
    <p class="txt txt--orange" style="left:516px; top:1078px; font-size:54px;">Flirty</p>
    <p class="txt txt--orange" style="left:538px; top:1128px; font-size:54px;">Presence</p>

    <!-- life purpose -->
    <p class="txt txt--orange" style="left:50px; top:902px; font-size:22px;">The purpose of my life is</p>
    <div class="block" style="left:0; top:926px; width:470px; height:66px;"></div>
    <p class="txt txt--white" style="left:10px; top:932px; font-size:58px;">To be loving courageous</p>
    <p class="txt txt--orange" style="left:14px; top:992px; font-size:118px;">Fun!</p>
    <p class="txt txt--orange" style="left:214px; top:1004px; font-size:40px;">I seek adventure</p>
    <div class="block" style="left:210px; top:1042px; width:282px; height:4px;"></div>
    <div class="block" style="left:208px; top:1050px; width:290px; height:52px;"></div>
    <p class="txt txt--white" style="left:216px; top:1054px; font-size:50px;">Laugh and play</p>
    <p class="txt txt--orange" style="left:18px; top:1106px; font-size:80px;">And live in God's</p>
    <p class="txt txt--orange" style="left:258px; top:1162px; font-size:80px;">Identity</p>

  </div>
</main>
</body>
</html>
```